2 page PSD web design

I need a fairly simple website design built in PSD format for a site / blog in the finance niche. My current web address is www.velmarquest.com. Velmar Quest Hub is a site that teaches people how to trade options with a focus on income strategies.

I need a simple homepage built and then another similar template for all other pages including blog posts.

The rough design layout is shown attached excel file. It is similar to www.dorentakessly.com although I don't like the colors on his site at all. My logo is attached also, so the colours should be aligned with my logo.

In the header section, I will be giving away a free ebook called "No-Fluff Manual for Calendar Spreads" so I will need a 2D and 3D book cover designed as well. The design should be aligned with my logo and site design.

Industry/Entity Type

Finance

Requirements
Must have
• Everything is detailed in the excel file, but here is a list of must have items:

My current logo
ebook design and sign up section
under the ebook sign up section, need a big bold heading - "HELPING YOU TRADE IRON CONDORS AND OTHER INCOME STRATEGIES WITHOUT THE BS"
6 sidebar sections as detailed in excel file
Social Proof at top right, on the same line / level as the logo
"home advertise contact" in the top left in small discreet font
Should not have
• Do not want any photos or images on either of the pages

```html
<!DOCTYPE html>
<html lang="en">
<head>
<meta charset="utf-8">
<title>Velmar Quest Hub</title>
<link href="https://fonts.googleapis.com/css2?family=Anton&family=Arimo:wght@400;700&family=Oswald:wght@500;700&display=swap" rel="stylesheet">
<style>
:root{
  --ink:#1b1b1b;
  --text:#333;
  --muted:#666;
  --blue:#1f86d4;
  --blue-dark:#0f5e9e;
  --blue-light:#cfe8fa;
  --blue-band:#8ccaf2;
  --red:#dd1f1f;
  --red-dark:#a81010;
  --bar:#1a1a1a;
  --nav:#2e2e2e;
  --page:#e4e4e4;
  --white:#fff;
  --line:#c9d9e6;
}
*{box-sizing:border-box;margin:0;padding:0}
html,body{width:1200px;height:2559px;overflow:hidden;background:var(--page)}
body{font-family:"Arimo",Arial,sans-serif;color:var(--text)}
.canvas{position:relative;width:1200px;height:2559px;overflow:hidden;background:var(--page)}

/* top utility bar */
.utility-bar{position:absolute;left:0;top:0;width:1200px;height:40px;background:var(--bar);display:flex;align-items:center;padding-left:34px;gap:34px}
.utility-bar a{color:#eee;font-size:15px;text-decoration:none}

/* header */
.site-header{position:absolute;left:0;top:40px;width:1200px;height:130px;background:var(--white)}
.brand{position:absolute;left:40px;top:36px;display:flex;align-items:center;gap:16px}
.brand-mark{width:58px;height:58px;border-radius:50%;background:var(--blue)}
.brand-name{font-family:"Arimo",Arial,sans-serif;font-weight:700;font-size:40px;color:var(--blue-dark)}
.social-proof{position:absolute;right:40px;top:12px;text-align:right;color:var(--ink);font-size:30px;line-height:34px}
.social-icons{display:flex;justify-content:flex-end;gap:8px;margin-top:8px}
.social-icons span{width:34px;height:34px;border-radius:5px;background:var(--blue)}
.social-icons span:nth-child(3){background:var(--red)}
.social-icons span:nth-child(4){background:#c0392b}

/* nav */
.main-nav{position:absolute;left:0;top:170px;width:1200px;height:45px;background:linear-gradient(#3a3a3a,#222);display:flex;align-items:center;padding-left:34px;gap:30px}
.main-nav a{color:#fff;font-size:15px;text-decoration:none}

/* hero */
.hero{position:absolute;left:0;top:215px;width:1200px;height:397px;background:linear-gradient(#d7d7d7,#bdbdbd)}
.hero-box{position:absolute;left:80px;top:13px;width:1072px;height:370px;background:var(--white);border-radius:10px;box-shadow:0 2px 8px rgba(0,0,0,.3)}
.hero-title{position:absolute;left:0;top:14px;width:100%;text-align:center;font-family:"Anton",Impact,sans-serif;font-size:46px;color:var(--ink);letter-spacing:.3px}
.ebook-art{position:absolute;left:40px;top:90px;width:580px;height:240px;border-radius:0 0 200px 0;background:linear-gradient(120deg,#f2f8fd 0%,#cfe6f8 55%,#7fbde9 100%)}
.ebook-cover{position:absolute;left:70px;top:105px;width:190px;height:210px;background:linear-gradient(135deg,#2e96e0,#0d4f88);box-shadow:8px 8px 14px rgba(0,0,0,.35)}
.hero-pitch{position:absolute;left:300px;top:112px;width:330px;font-size:23px;line-height:28px;color:var(--ink)}
.hero-pitch strong{color:var(--red);font-weight:700}
.hero-note{position:absolute;left:330px;top:210px;width:300px;font-size:15px;line-height:19px;color:var(--ink)}
.signup{position:absolute;left:660px;top:78px;width:380px;height:276px;border-radius:10px;background:linear-gradient(#49aef0,#1a78c7);padding:0 18px}
.signup-head{margin:0 -18px;height:54px;border-radius:10px 10px 0 0;background:linear-gradient(#8fd0f8,#5db7ef);text-align:center;font-family:"Anton",Impact,sans-serif;font-size:30px;line-height:54px;color:var(--ink)}
.signup-head em{font-style:normal;color:var(--red)}
.signup-field{display:block;margin-top:14px;height:38px;background:var(--white);border:1px solid #9cc;padding-left:12px;font-size:17px;line-height:38px;color:#999}
.signup-button{display:block;margin:18px auto 0;width:300px;height:54px;border-radius:8px;background:linear-gradient(#f04848,#c41212);border:2px solid #fff;text-align:center;color:#fff;font-size:30px;line-height:50px}
.signup-privacy{margin-top:8px;text-align:center;font-size:10px;color:#eaf4fb}

/* banner */
.tagline-band{position:absolute;left:0;top:620px;width:1200px;height:105px;background:linear-gradient(#b6def8,var(--blue-band));display:flex;align-items:center;justify-content:center;text-align:center}
.tagline-band h1{font-family:"Anton",Impact,sans-serif;font-weight:400;font-size:35px;line-height:42px;color:#fff;letter-spacing:.6px;text-shadow:-2px -2px 0 var(--blue-dark),2px -2px 0 var(--blue-dark),-2px 2px 0 var(--blue-dark),2px 2px 0 var(--blue-dark)}

/* post cards */
.post-card{position:absolute;left:34px;width:848px;background:var(--white);padding:16px 26px 0;box-shadow:0 2px 6px rgba(0,0,0,.2)}
.latest{top:734px;height:900px}
.featured{top:1692px;height:811px}
.section-title{font-size:27px;color:var(--blue);border-bottom:2px solid var(--line);padding-bottom:4px;margin-bottom:12px}
.post{border-bottom:1px dotted #bbb;padding-bottom:12px;margin-bottom:14px}
.post:last-child{border-bottom:0}
.post-title{font-size:27px;line-height:34px;color:var(--ink);font-weight:400;margin-bottom:10px}
.post-row{display:flex;gap:24px}
.post-thumb{flex:0 0 316px;height:160px}
.thumb-market{background:linear-gradient(135deg,#041a3e,#1864c2 55%,#7cc4ff)}
.thumb-decline{background:linear-gradient(160deg,#e85a3a,#f0a080 50%,#4ea24a)}
.post-body{flex:1;font-size:13px;line-height:17px;color:var(--text)}
.post-meta{margin-bottom:12px}
.post-meta a{color:var(--blue);text-decoration:none}
.read-more{display:block;width:90px;margin:6px 0 0 auto;height:26px;border-radius:4px;background:linear-gradient(#5cb6f0,#1f86d4);color:#fff;font-size:14px;line-height:26px;text-align:center}
.featured .post{margin-bottom:10px;padding-bottom:10px}
.featured .post-title{margin-bottom:8px}

/* sidebar */
.widget{position:absolute;left:893px;width:273px;background:linear-gradient(#fff,var(--blue-light));border:3px solid #9fd0f2;border-radius:8px;text-align:center;padding:10px 16px}
.widget-title{font-family:"Oswald",sans-serif;font-weight:700;font-size:36px;line-height:42px;color:var(--blue)}
.widget-title .accent{color:var(--red)}
.widget-sub{font-family:"Oswald",sans-serif;font-weight:500;font-size:22px;color:var(--blue);font-style:italic;margin-top:-4px}
.widget p{font-size:15px;line-height:19px;color:var(--text);margin:12px 0}
.cta{display:block;margin:0 auto;width:200px;height:50px;border-radius:6px;background:linear-gradient(#ec2a2a,#b80f0f);border:2px solid #fff;color:#fff;font-family:"Oswald",sans-serif;font-weight:700;font-size:28px;line-height:46px}
.w-work{top:734px;height:204px}
.w-new{top:947px;height:199px}
.w-training{top:1155px;height:210px}
.training-list{list-style:none;margin-top:8px}
.training-list li{height:32px;margin-bottom:5px;background:linear-gradient(#e8f5fd,#b9dff7);border:1px solid #9fd0f2;font-size:14px;line-height:30px;color:var(--ink)}
.w-sponsors{top:1394px;height:250px}
.sponsor-grid{display:grid;grid-template-columns:1fr 1fr;gap:10px;margin-top:12px}
.sponsor-grid span{height:72px;display:flex;align-items:center;justify-content:center;font-size:18px;font-weight:700;color:var(--blue-dark)}
.w-ad{top:1655px;height:236px}
.ad-brand{display:flex;align-items:center;justify-content:center;gap:8px;font-size:24px;font-weight:700;color:var(--blue-dark);margin-top:8px}
.ad-brand i{width:22px;height:22px;background:var(--blue)}
.ad-line{font-size:20px!important;line-height:24px!important;color:var(--ink)!important}
.w-ad .cta{font-size:24px}
.w-news{top:1900px;height:205px;text-align:left}
.w-news p{margin:4px 0 10px;font-size:14px;line-height:18px}
.w-news label{display:block;font-weight:700;font-size:14px;color:var(--ink)}
.news-field{height:26px;background:#fff;border:1px solid #9cc;margin:4px 0 10px}
.news-button{display:block;width:110px;height:30px;margin-left:auto;background:linear-gradient(#e83030,#b80f0f);color:#fff;font-size:14px;font-weight:700;line-height:30px;text-align:center;border-radius:3px}

/* footer */
.site-footer{position:absolute;left:0;top:2525px;width:1200px;height:34px;background:var(--bar);color:#ddd;font-size:13px;line-height:34px;text-align:center}
</style>
</head>
<body>
<div class="canvas">

  <nav class="utility-bar">
    <a>Home</a><a>Advertise</a><a>Contact</a>
  </nav>

  <header class="site-header">
    <div class="brand"><span class="brand-mark"></span><span class="brand-name">Velmar Quest Hub</span></div>
    <div class="social-proof">Join a Community of<br>4279 Awesome Readers
      <div class="social-icons"><span></span><span></span><span></span><span></span></div>
    </div>
  </header>

  <nav class="main-nav">
    <a>Articles and Videos</a><a>Trading Philosophy</a><a>Learning Centre</a><a>Free Tools</a><a>Members Only</a><a>Work With Us</a><a>About</a>
  </nav>

  <section class="hero">
    <div class="hero-box">
      <h2 class="hero-title">Do You Want To Know The Truth About Iron Condors?</h2>
      <div class="ebook-art" role="img" aria-label="Blue swoosh arrow sweeping behind the ebook"></div>
      <div class="ebook-cover" role="img" aria-label="3D cover of the ebook No-Fluff Manual for Calendar Spreads"></div>
      <p class="hero-pitch">Learn How To Trade This Amazing Option Income Strategy With My <strong>FREE</strong> Ebook</p>
      <p class="hero-note">I will share with you my blueprint and all my tips and tricks for generating consistent monthly income with iron condors</p>
      <form class="signup">
        <div class="signup-head">Get The Ebook <em>NOW!!</em></div>
        <span class="signup-field">Enter your name</span>
        <span class="signup-field">Enter your email address</span>
        <span class="signup-button">Instant Access</span>
        <div class="signup-privacy">Your information is never shared or sold for any reason</div>
      </form>
    </div>
  </section>

  <section class="tagline-band">
    <h1>HELPING YOU TRADE IRON CONDORS AND OTHER INCOME STRATEGIES<br>WITHOUT THE BS</h1>
  </section>

  <main>
    <section class="post-card latest">
      <h2 class="section-title">Latest Posts</h2>
      <article class="post">
        <h3 class="post-title">GBP/USD: UK mortgage approvals rose less-than-expected in November, indicates ALC</h3>
        <div class="post-row">
          <div class="post-thumb thumb-market" role="img" aria-label="Blue stock market price board"></div>
          <div class="post-body">
            <div class="post-meta">Posted by : <a>Marcus</a></div>
            For the 24 hours to 23:00 GMT, GBP fell marginally against the USD and closed at 1.6114, after UK's Albion Lenders' Council (ALC) reported that the number of new mortgages approved in November rose to 33,634 approvals from the 24 hours to 23:00 GMT, GBP fell marginally against the USD and closed at 1.6114 ...
            <span class="read-more">Read More</span>
          </div>
        </div>
      </article>
      <article class="post">
        <h3 class="post-title">GBP/USD: UK mortgage approvals rose less-than-expected in November, indicates ALC</h3>
        <div class="post-row">
          <div class="post-thumb thumb-market" role="img" aria-label="Blue stock market price board"></div>
          <div class="post-body">
            <div class="post-meta">Posted by : <a>Marcus</a></div>
            For the 24 hours to 23:00 GMT, GBP fell marginally against the USD and closed at 1.6114, after UK's Albion Lenders' Council (ALC) reported that the number of new mortgages approved in November rose to 33,634 approvals from the 24 hours to 23:00 GMT, GBP fell marginally against the USD and closed at 1.6114 ...
            <span class="read-more">Read More</span>
          </div>
        </div>
      </article>
      <article class="post">
        <h3 class="post-title">GBP/USD: UK mortgage approvals rose less-than-expected in November, indicates ALC</h3>
        <div class="post-row">
          <div class="post-thumb thumb-market" role="img" aria-label="Blue stock market price board"></div>
          <div class="post-body">
            <div class="post-meta">Posted by : <a>Marcus</a></div>
            For the 24 hours to 23:00 GMT, GBP fell marginally against the USD and closed at 1.6114, after UK's Albion Lenders' Council (ALC) reported that the number of new mortgages approved in November rose to 33,634 approvals from the 24 hours to 23:00 GMT, GBP fell marginally against the USD and closed at 1.6114 ...
            <span class="read-more">Read More</span>
          </div>
        </div>
      </article>
    </section>

    <section class="post-card featured">
      <h2 class="section-title">Featured Posts</h2>
      <article class="post">
        <h3 class="post-title">USD/CHF: Halvern Bank consumption indicator slipped in November</h3>
        <div class="post-row">
          <div class="post-thumb thumb-decline" role="img" aria-label="Red downward arrow over a green chart"></div>
          <div class="post-body">
            <div class="post-meta">Posted by : <a>Marcus</a></div>
            For the 24 hours to 23:00 GMT, the USD declined marginally against the CHF and closed at 0.9126. In Switzerland, the Halvern Bank consumption indicator retreated to 1.23 in November, from 1.30 in October. In the Asian session, at GMT0400 for the 24 hours to 23:00 GMT, the USD declined marginally against the CHF and closed at ...
            <span class="read-more">Read More</span>
          </div>
        </div>
      </article>
      <article class="post">
        <h3 class="post-title">USD/CHF: Halvern Bank consumption indicator slipped in November</h3>
        <div class="post-row">
          <div class="post-thumb thumb-decline" role="img" aria-label="Red downward arrow over a green chart"></div>
          <div class="post-body">
            <div class="post-meta">Posted by : <a>Marcus</a></div>
            For the 24 hours to 23:00 GMT, the USD declined marginally against the CHF and closed at 0.9126. In Switzerland, the Halvern Bank consumption indicator retreated to 1.23 in November, from 1.30 in October. In the Asian session, at GMT0400 for the 24 hours to 23:00 GMT, the USD declined marginally against the CHF and closed at ...
            <span class="read-more">Read More</span>
          </div>
        </div>
      </article>
      <article class="post">
        <h3 class="post-title">USD/CHF: Halvern Bank consumption indicator slipped in November</h3>
        <div class="post-row">
          <div class="post-thumb thumb-decline" role="img" aria-label="Red downward arrow over a green chart"></div>
          <div class="post-body">
            <div class="post-meta">Posted by : <a>Marcus</a></div>
            For the 24 hours to 23:00 GMT, the USD declined marginally against the CHF and closed at 0.9126. In Switzerland, the Halvern Bank consumption indicator retreated to 1.23 in November, from 1.30 in October. In the Asian session, at GMT0400 for the 24 hours to 23:00 GMT, the USD declined marginally against the CHF and closed at ...
            <span class="read-more">Read More</span>
          </div>
        </div>
      </article>
    </section>
  </main>

  <aside>
    <section class="widget w-work">
      <div class="widget-title">Work with us</div>
      <div class="widget-sub">One-one-one</div>
      <p>We're ready to help you achieve the success you're looking for</p>
      <span class="cta">CLICK HERE</span>
    </section>
    <section class="widget w-new">
      <div class="widget-title">New to Options ?</div>
      <p>Check out our comprehensive training program</p>
      <span class="cta">CLICK HERE</span>
    </section>
    <section class="widget w-training">
      <div class="widget-title"><span class="accent">Free</span> Training</div>
      <ul class="training-list">
        <li>Volatility Tutorials</li>
        <li>Iron Condor Tutorials</li>
        <li>Income Trading Tutorials</li>
        <li>Free Tools and Resources</li>
      </ul>
    </section>
    <section class="widget w-sponsors">
      <div class="widget-title">Top Sponsors</div>
      <div class="sponsor-grid">
        <span>Brightmark Studio</span><span>Norlane Systems</span>
        <span>Quorra</span><span>Pellix</span>
      </div>
    </section>
    <section class="widget w-ad">
      <div class="ad-brand"><i></i>Brightmark Studio</div>
      <p class="ad-line">The #1 design marketplace online</p>
      <p class="ad-line">Get 25 % Off Design</p>
      <span class="cta">Start Here</span>
    </section>
    <section class="widget w-news">
      <p>Stay up to date with Velmar Quest Hub. New articles and tutorials delivered straight to your inbox</p>
      <label>Email address</label>
      <div class="news-field"></div>
      <span class="news-button">Let's Do This</span>
    </section>
  </aside>

  <footer class="site-footer">Copyright © Velmar Quest Hub</footer>
</div>
</body>
</html>
```